Vell Partners Building Business Cards

We need a business card that reflects our business as "Solar Experts" in San Diego. Browse our website www.vellpartners.example our License needs to be displayed as "CSLB# 4718392" our phone number is (619) 555-0147

Save thousands on your electric bills and increase the value of your home while helping to protect the environment. Our solar installation experts will help you design the system that's right for you, using only the highest quality equipment that will look great and give you ideal performance. Our goal is to make you energy independent, and get your electric bill to 0.

Tobias Wrenfield
(619) 555-0147
tobias@vellpartners.example

Target Market(s)

Home owners in san diego looking for solar

Industry/Entity Type

Solar Energy

Contact Information for Business Card

Tobias Wrenfield
(619) 555-0147
tobias@vellpartners.example

Font styles to use
Other font styles liked:
• Use our logo font

Requirements
Must have
• License needs to be displayed as "CSLB# 4718392" our phone number is (619) 555-0147
Nice to have
• Real images of rooftop home solar in san diego
Should not have
• our business address

```html
<!DOCTYPE html>
<html lang="en">
<head>
<meta charset="utf-8">
<title>Vell Partners Building – Business Card</title>
<link rel="stylesheet" href="https://fonts.googleapis.com/css2?family=Questrial&family=Arimo:wght@400;700&display=swap">
<style>
  :root {
    --backdrop: #2b2b2d;
    --card-white: #ffffff;
    --navy: #1e3f7d;
    --navy-deep: #163166;
    --sun-yellow: #f5ab00;
    --text-light: #ffffff;
  }
  html, body {
    margin: 0;
    padding: 0;
    width: 1200px;
    height: 950px;
    overflow: hidden;
    background: var(--backdrop);
  }
  .canvas {
    position: relative;
    width: 1200px;
    height: 950px;
  }
  .card {
    position: absolute;
    top: 125px;
    width: 400px;
    height: 700px;
    overflow: hidden;
    border-radius: 2px;
    box-shadow: 0 10px 30px rgba(0,0,0,0.45);
  }
  /* Front */
  .card-front {
    left: 160px;
    background: var(--card-white);
  }
  .brand-name {
    position: absolute;
    top: 120px;
    left: 0;
    width: 100%;
    text-align: center;
    font-family: "Questrial", sans-serif;
    font-size: 34px;
    line-height: 1.1;
    color: var(--navy);
  }
  .front-wave {
    position: absolute;
    left: 0;
    top: 0;
    width: 400px;
    height: 700px;
  }
  .contact {
    position: absolute;
    top: 470px;
    left: 0;
    width: 100%;
    text-align: center;
    font-family: "Arimo", sans-serif;
    color: var(--text-light);
    font-size: 17px;
    line-height: 1.6;
  }
  .contact .person-name {
    font-weight: 700;
    font-size: 22px;
    color: var(--sun-yellow);
    margin-bottom: 2px;
  }
  .contact .label {
    color: var(--sun-yellow);
    font-weight: 700;
  }
  .contact p { margin: 0; }
  /* Back */
  .card-back {
    left: 640px;
    background: var(--sun-yellow);
  }
  .back-web {
    position: absolute;
    left: 38px;
    top: 190px;
    transform-origin: left top;
    transform: rotate(90deg) translateY(-100%);
    font-family: "Arimo", sans-serif;
    font-size: 15px;
    letter-spacing: 3px;
    color: var(--text-light);
    white-space: nowrap;
  }
  .back-brand {
    position: absolute;
    top: 300px;
    left: 60px;
    width: 300px;
    text-align: center;
    font-family: "Questrial", sans-serif;
    font-size: 38px;
    line-height: 1.15;
    color: var(--text-light);
  }
</style>
</head>
<body>
<main class="canvas">
  <section class="card card-front">
    <div class="brand-name">Vell Partners Building</div>
    <svg class="front-wave" viewBox="0 0 400 700" aria-hidden="true">
      <path d="M0 360 C 110 330, 200 400, 400 380 L400 700 L0 700 Z" fill="var(--navy)"/>
      <path d="M0 360 C 110 330, 200 400, 400 380" fill="none" stroke="var(--sun-yellow)" stroke-width="6"/>
    </svg>
    <div class="contact">
      <p class="person-name">Tobias Wrenfield</p>
      <p>CEO/Founder</p>
      <p>CSLB# 4718392</p>
      <p><span class="label">P:</span> (619) 555-0147</p>
      <p><span class="label">E:</span> tobias@vellpartners.example</p>
      <p><span class="label">W:</span> www.vellpartners.example</p>
    </div>
  </section>

  <section class="card card-back">
    <div class="back-web">www.vellpartners.example</div>
    <div class="back-brand">Vell Partners Building</div>
  </section>
</main>
</body>
</html>
```